Flyer-Design für Neueröffnung eines Online-Shops
Zielgruppe
Ich verkaufe Online Lebensmittel, die normalerweise entsorgt werden, da das Mindesthaltbarkeitsdatum (MHD ) entweder in Kürze abläuft oder bereits überschritten ist, obwohl diese noch genießbar sind.
Der Fokus liegt auf nicht kühlbedürftige Ware wie Getränke, Süßwaren, Cerealien, Konserven, Gewürze, Getreidetrockenprodukte. Hinzu kommen Sonderposten aus Geschäftsauflösungen, Überproduktionen usw.
Das Ziel ist es, die Lebensmittelverschwendung zu reduzieren und der Bevölkerung, genießbare Lebensmittel zu einem geringen Preis anzubieten.
Die beiden Hauptzielgruppen sind;
1. Umweltbewusste Personen, die die Reduzierung der Lebensmittelverschwendung unterstützen wollen
2. Personen aus dem Niedriglohnsektor, die jeden Euro 'zweimal' umdrehen müssen und sich keine Markenware leisten können.
Aufgabenstellung
Der Onlineshop startet im Januar, das bedeutet der Onlineshop ist noch nicht bekannt. Daher soll der Flyer einem sofort ins Auge fallen. Jedoch soll auf dem Flyer nicht erwähnt werden, dass es sich um einen 'Neueröffnung' handelt.
Jedoch fahre ich eine Eröffnungsaktion, die jedoch als 'Januar' Special' oder Neujahrsspecial' o.ä. betitelt werden soll. Nämlich 'versandkostenfreie Lieferung ab 10€ Warenwert*'
*gilt für Bestellungen bis zum 31.01.18
Folgende Inhalte sollten im Design vorkommen:
Das Logo, der Slogan ' Verschwendung reduzieren, Ersparnis maximieren', die Domain 'www.kor-tibu.de' + der Hinweis auf die versandkostenfreie Lieferung am 10€ Warenwert im Januar.
Folgende Inhalte sind optional:
Stichwörter wie 'nachhaltig', 'umweltbewusst', 'bis zu 70% Ersparnis', '82kg Lebensmittel werden jährlich pro Person entsorgt',
Als Farbton sollte grün im Vordergrund stehen, gerne in zwei verschiedenen Helligkeitsstufen. Als Kontrastfarben wären Ideen rot( für den Rabatt/Ersparnis und da es sich um MHD nahe Lebensmittel handelt ) und schwarz oder weiß.
Der Flyer wird im A5 Hochformat gedruckt ( Querformat bei Bedarf auch möglich ). Dicke = voraussichtlich 300gr (alternativ 250gr ), 2-seitig
Ich werde das Logo und eine erste Skizze von einer Flyervorlage. Die Flyervorlage soll jedoch nur als Unterstützung für die Farbgebung dienen. Bitte die Designs unabhängig davon gestalten und diese evtl als kleine 'Hilfe' nutzen.
Da das Thema recht erklärungsbedürftig ist, ist meine Idee auf der Rückseite eine Art Begriffsklärung zu erstellen. Eine Vorlage für den Inhalt habe ich erstellt und wird ebenfalls hochgeladen. Jedoch soll die Begriffsklärung nicht einfach runtergeschrieben werden sondern kreativ eingebaut/verpackt werden ( z.B. Sprechblasen oder Emojis, Cliparts o.ä. )
Der Kunde soll sofort sehen, dass es darum geht die Lebensmittelverschwendung zu reduzieren und im gleichen Zuge genießb..

```html
<!DOCTYPE html>
<html lang="de">
<head>
<meta charset="utf-8">
<title>Kor Tibu – Verschwendung minimieren</title>
<link rel="stylesheet" href="https://fonts.googleapis.com/css2?family=Archivo:wdth,wght@62..125,500..900&display=swap">
<style>
  :root {
    --flyer-green: #4a8759;
    --ink-white: #ffffff;
    --ink-dark: #2a2a2a;
  }
  html, body {
    margin: 0;
    padding: 0;
    width: 851px;
    height: 1200px;
    overflow: hidden;
    background: var(--flyer-green);
  }
  .flyer {
    position: relative;
    width: 851px;
    height: 1200px;
    background: var(--flyer-green);
    font-family: "Archivo", "Helvetica Neue", Arial, sans-serif;
    color: var(--ink-white);
  }
  .slogan {
    position: absolute;
    left: 0;
    top: 0;
    width: 851px;
    height: 460px;
  }
  .slogan text {
    font-family: "Archivo", "Helvetica Neue", Arial, sans-serif;
    font-stretch: 112%;
    fill: var(--ink-white);
  }
  .slogan .line-light { font-weight: 600; }
  .slogan .line-heavy { font-weight: 900; }
  .fact {
    position: absolute;
    left: 0;
    top: 532px;
    width: 851px;
    margin: 0;
    text-align: center;
    font-size: 52px;
    line-height: 55px;
    font-weight: 700;
    font-stretch: 110%;
    letter-spacing: 0.5px;
  }
  .fact .amount { color: var(--ink-dark); }
  .mission {
    position: absolute;
    left: 0;
    top: 803px;
    width: 851px;
    margin: 0;
    text-align: center;
    font-size: 23px;
    line-height: 34px;
    font-weight: 700;
    font-stretch: 105%;
  }
  .brand {
    position: absolute;
    left: 0;
    top: 1050px;
    width: 851px;
    display: flex;
    justify-content: center;
    align-items: center;
    gap: 14px;
  }
  .brand-mark {
    width: 30px;
    height: 30px;
    background: var(--ink-white);
  }
  .brand-name {
    font-size: 44px;
    font-weight: 900;
    font-stretch: 112%;
    color: var(--ink-white);
    line-height: 1;
  }
</style>
</head>
<body>
  <main class="flyer">
    <svg class="slogan" viewBox="0 0 851 460" aria-label="Verschwendung minimieren, Ersparnisse maximieren">
      <text class="line-light" x="79" y="113" font-size="80" textLength="694" lengthAdjust="spacingAndGlyphs">VERSCHWENDUNG</text>
      <text class="line-heavy" x="81" y="229" font-size="128" textLength="691" lengthAdjust="spacingAndGlyphs">MINIMIEREN</text>
      <text class="line-light" x="83" y="327" font-size="110" textLength="690" lengthAdjust="spacingAndGlyphs">ERSPARNISSE</text>
      <text class="line-heavy" x="84" y="435" font-size="118" textLength="688" lengthAdjust="spacingAndGlyphs">MAXIMIEREN</text>
    </svg>

    <p class="fact">Jedes Jahr werden in<br>Deutschland <span class="amount">82&nbsp;kg</span> an<br>Lebensmitteln pro<br>Person entsorgt.</p>

    <p class="mission">Kor Tibu verkauft MHD-nahe Lebensmittel,<br>um die Lebensmittelverschwendung<br>zu stoppen.</p>

    <div class="brand">
      <span class="brand-mark"></span>
      <span class="brand-name">Kor Tibu</span>
    </div>
  </main>
</body>
</html>
```